'Bright Ledger Hidden Keys' Book Cover

I need a professional book cover design for my new upcoming book that shows people how to get a high credit score.

Here are my two websites:

https://www.moneywordbank-lexa.info
https://moneywordbank-lexa.com/

I am looking for a clean, professional design that pops (emotional touch) and separates from the other books that are on the market. Cover aspect ratio 1:4 for Pagewisp version and 1:5 for the paperback version. Yellow or blue are good colors - but not must. See the basic examples that I provided. File delivery format PDF.

Book Title: Bright Ledger Hidden Keys
Byline: The Quick Lift And Mend Manual for Stellar Borrowing

Currently on Brindlecart pre-order:
https://www.brindlecart.example/Bright-Ledger-Hidden-Keys-Stellar-ebook/dp/Q48MPLRT71

I am the author of 36 published books on Brindlecart. My author profile is here:
brindlecart.example/author/gideonvarly

Targeted audience: People that want to improve or repair their bad credit score.

Target Market(s)

People/consumers in the US that want to improve or repair their credit score.

Industry/Entity Type

Consumer

Font styles to use
Sans Serif

Colors

Designer to choose colors to be used in the design.

Requirements
Must have
• Author name, Title, byline, and graphic element(s).
Nice to have
• - 2020 edition logo / batch

```html
<!DOCTYPE html>
<html lang="en">
<head>
<meta charset="utf-8">
<title>Bright Ledger Hidden Keys – Book Cover</title>
<link rel="stylesheet" href="https://fonts.googleapis.com/css2?family=Roboto+Condensed:wght@400;700;800&display=swap">
<style>
  :root {
    --yellow-light: #ffe15a;
    --yellow-mid: #fcc70f;
    --yellow-deep: #f4b400;
    --title-white: #ffffff;
    --title-blue: #1a78cf;
    --ink: #111111;
    --gold-light: #f8e39a;
    --gold-mid: #d9b04c;
    --gold-dark: #a97b1c;
    --photo-top: #5a5550;
    --photo-mid: #b59a86;
    --photo-low: #ead2c2;
  }
  * { margin: 0; padding: 0; box-sizing: border-box; }
  html, body { width: 900px; height: 1200px; overflow: hidden; }
  body { font-family: "Roboto Condensed", "Arial Narrow", sans-serif; }

  .cover {
    position: relative;
    width: 900px;
    height: 1200px;
    overflow: hidden;
    background: radial-gradient(ellipse 70% 55% at 50% 62%, var(--yellow-light) 0%, var(--yellow-mid) 55%, var(--yellow-deep) 100%);
  }

  .cover-title {
    position: absolute;
    top: 14px;
    left: 0;
    width: 100%;
    text-align: center;
    font-weight: 800;
    text-transform: uppercase;
    font-size: 132px;
    line-height: 124px;
    letter-spacing: -1px;
  }
  .cover-title .line { display: block; color: var(--title-white); }
  .cover-title .line--accent { color: var(--title-blue); }

  .cover-subtitle {
    position: absolute;
    top: 400px;
    left: 0;
    width: 100%;
    text-align: center;
    color: var(--ink);
    font-weight: 700;
    text-transform: uppercase;
    font-size: 46px;
    line-height: 52px;
  }
  .cover-subtitle span { display: block; }

  .hero-photo {
    position: absolute;
    left: 0;
    top: 530px;
    width: 570px;
    height: 670px;
    border-top-right-radius: 40px;
    background: linear-gradient(180deg, var(--photo-top) 0%, var(--photo-mid) 40%, var(--photo-low) 75%, var(--photo-low) 100%);
    opacity: 0.85;
  }

  .edition-seal {
    position: absolute;
    left: 578px;
    top: 888px;
    width: 182px;
    height: 182px;
    border-radius: 50%;
    background: radial-gradient(circle at 40% 35%, var(--gold-light) 0%, var(--gold-mid) 55%, var(--gold-dark) 100%);
    display: flex;
    flex-direction: column;
    align-items: center;
    justify-content: center;
    color: var(--ink);
    font-weight: 400;
    font-size: 32px;
    line-height: 36px;
    text-align: center;
  }

  .cover-author {
    position: absolute;
    right: 50px;
    top: 1104px;
    color: var(--ink);
    font-weight: 800;
    text-transform: uppercase;
    font-size: 64px;
    line-height: 64px;
    letter-spacing: 0.5px;
  }
</style>
</head>
<body>
  <main class="cover">
    <h1 class="cover-title">
      <span class="line">Bright Ledger</span>
      <span class="line">Hidden</span>
      <span class="line line--accent">Keys</span>
    </h1>
    <p class="cover-subtitle">
      <span>The Quick Lift And Mend Manual</span>
      <span>for Stellar Borrowing</span>
    </p>
    <div class="hero-photo" role="img" aria-label="Photo of a hand holding up a dark payment card"></div>
    <div class="edition-seal">
      <span>2020</span>
      <span>Edition</span>
    </div>
    <p class="cover-author">Gideon Varly</p>
  </main>
</body>
</html>
```